Salon and Spa Distributor Business Card

Need a business card. We are are distributor in the salon and spa industry. We identify with natural beauty. Need a card with:
Company Name: Petal Haven"
Title: "President & CEO"
Address
Company Phone number
email
website
Tag Line:" The Professional Salon Source"

Industry/Entity Type

Business

Contact Information for Business Card

Name: Lena Morcott
Title: "President & CEO"
Address: 317 Birchfield Ln, Oakvane, NJ 07481
Company Phone number: 800-463-9152
email: lenamorcott@petalhaven-example.com
website: www.petalhaven-example.com

Requirements
Should not have
• No black backgrounds

```html
<!DOCTYPE html>
<html lang="en">
<head>
<meta charset="utf-8">
<title>Petal Haven — Business Card</title>
<link rel="stylesheet" href="https://fonts.googleapis.com/css2?family=Raleway:wght@300;500&family=Archivo:wght@400&display=swap">
<style>
  :root {
    --teal: #49c1bb;
    --teal-deep: #2f9f9a;
    --cream: #f8f6d8;
    --white: #ffffff;
    --ink: #4a5a58;
    --leaf-light: #7cf23a;
    --leaf-mid: #5fd82a;
    --leaf-deep: #2f9e1e;
  }
  html, body {
    margin: 0;
    padding: 0;
    width: 1200px;
    height: 720px;
    overflow: hidden;
    background: var(--white);
  }
  .card {
    position: relative;
    width: 1200px;
    height: 720px;
    background: var(--white);
    overflow: hidden;
  }
  .card__wave {
    position: absolute;
    inset: 0;
    width: 1200px;
    height: 720px;
  }
  .card__wave-fill { fill: var(--teal); }
  .card__emblem {
    position: absolute;
    left: 20px;
    top: 50px;
    width: 520px;
    height: 600px;
  }
  .brand-name {
    position: absolute;
    right: 28px;
    top: 92px;
    margin: 0;
    font-family: "Raleway", sans-serif;
    font-weight: 300;
    font-size: 86px;
    line-height: 1;
    letter-spacing: 0.01em;
    color: var(--cream);
    white-space: nowrap;
  }
  .contact {
    position: absolute;
    right: 28px;
    top: 312px;
    margin: 0;
    text-align: right;
    font-style: normal;
    font-family: "Raleway", sans-serif;
    color: var(--ink);
  }
  .contact__name {
    display: block;
    font-weight: 500;
    font-size: 30px;
    line-height: 36px;
    color: var(--teal-deep);
  }
  .contact__title {
    display: block;
    font-weight: 300;
    font-size: 20px;
    line-height: 26px;
    margin-bottom: 12px;
    color: var(--teal-deep);
  }
  .contact__line {
    display: block;
    font-weight: 300;
    font-size: 18px;
    line-height: 25px;
    white-space: nowrap;
  }
  .tagline {
    position: absolute;
    left: 840px;
    top: 530px;
    margin: 0;
    font-family: "Archivo", sans-serif;
    font-weight: 400;
    font-size: 29px;
    line-height: 43px;
    letter-spacing: 0.2em;
    color: var(--teal);
  }
  .tagline span { display: block; }
</style>
</head>
<body>
  <div class="card">
    <svg class="card__wave" viewBox="0 0 1200 720" aria-hidden="true">
      <path class="card__wave-fill" d="M0,0 H1200 V176 C1080,250 980,292 860,283 C640,268 460,40 250,28 C130,22 50,60 0,118 Z"/>
    </svg>

    <svg class="card__emblem" viewBox="0 0 520 600" role="img" aria-label="Green illustration of a woman's profile with flowing hair and leaves">
      <defs>
        <linearGradient id="emblemGreen" x1="0" y1="0" x2="1" y2="1">
          <stop offset="0" stop-color="var(--leaf-light)"/>
          <stop offset="0.6" stop-color="var(--leaf-mid)"/>
          <stop offset="1" stop-color="var(--leaf-deep)"/>
        </linearGradient>
      </defs>
      <ellipse cx="260" cy="300" rx="250" ry="290" fill="url(#emblemGreen)" opacity="0.85"/>
    </svg>

    <h1 class="brand-name">Petal Haven</h1>

    <address class="contact">
      <span class="contact__name">Lena Morcott</span>
      <span class="contact__title">President &amp; CEO</span>
      <span class="contact__line">317 Birchfield Ln, Oakvane, NJ 07481</span>
      <span class="contact__line">800-463-9152</span>
      <span class="contact__line">lenamorcott@petalhaven-example.com</span>
      <span class="contact__line">www.petalhaven-example.com</span>
    </address>

    <p class="tagline">
      <span>The</span>
      <span>Professional</span>
      <span>Salon Source</span>
    </p>
  </div>
</body>
</html>
```